The Lantern Pact a non-fiction book on mindfulness COVER design needed

A non-fiction book about active mindfulness.
The Lantern Pact includes 21 different daily 'dares' which are action based activities to generate positive mindfulness - to become more contented with life.
Based on the teeaching of the New Thought movements of the early 20th century, think The Hollow, Climb and Gather Plenty.
The book is positive and uplifting. It fits into the self-help / spiritual / health segments. It skews female 40 to 50 year olds.
Think fresh colours like a bold orange or bright green.
What needs to be on the cover:
TITLE: The Lantern Pact
AUTHOR: Marcus Tindall
BLURB: Get clarity, focus, and a new zest for life by following The Lantern Pact for just 21 days.
Target Market(s)
Women 40-50 english speaking
Industry/Entity Type
Self-help / Health

```html
<!DOCTYPE html>
<html lang="en">
<head>
<meta charset="utf-8">
<title>The Lantern Pact – Cover Options</title>
<link rel="stylesheet" href="https://fonts.googleapis.com/css2?family=Antonio:wght@100;200&family=EB+Garamond:wght@400&display=swap">
<style>
  :root {
    --page: #ffffff;
    --orange: #f15a2b;
    --green: #72b84c;
    --red: #ee4136;
    --lime: #c4d843;
    --amber: #f7941d;
    --ink: #4a4a4a;
    --ink-dark: #333333;
    --frame: #222222;
    --white: #ffffff;
  }
  * { margin: 0; padding: 0; box-sizing: border-box; }
  html, body {
    width: 1200px;
    height: 1000px;
    overflow: hidden;
    background: var(--page);
  }
  .board {
    position: relative;
    width: 1200px;
    height: 1000px;
  }
  .cover {
    position: absolute;
    width: 297px;
    height: 445px;
    border: 1px solid var(--frame);
    text-align: center;
  }
  .cover--white-orange { left: 272px; top: 40px; background: var(--white); --title: var(--orange); --rule: var(--lime); --author: var(--ink); --blurb: var(--ink-dark); }
  .cover--white-green  { left: 615px; top: 40px; background: var(--white); --title: var(--green); --rule: var(--amber); --author: var(--ink); --blurb: var(--ink-dark); }
  .cover--green        { left: 272px; top: 511px; background: var(--green); border-color: #8cc56b; --title: var(--orange); --rule: var(--lime); --author: var(--white); --blurb: var(--white); }
  .cover--red          { left: 615px; top: 511px; background: var(--red); --title: var(--green); --rule: var(--amber); --author: var(--white); --blurb: var(--white); }

  .cover__author {
    position: absolute;
    left: 0; right: 0; top: 20px;
    font-family: "EB Garamond", Georgia, serif;
    font-size: 31px;
    line-height: 40px;
    color: var(--author);
  }
  .cover__rule {
    position: absolute;
    left: 50%;
    width: 47px;
    height: 2px;
    margin-left: -23px;
    background: var(--rule);
  }
  .cover__rule--top { top: 79px; }
  .cover__rule--bottom { top: 365px; }
  .cover__title {
    position: absolute;
    left: 0; right: 0; top: 96px;
    font-family: "Antonio", "Arial Narrow", sans-serif;
    font-weight: 100;
    font-size: 86px;
    line-height: 86px;
    color: var(--title);
    text-transform: uppercase;
    letter-spacing: 1px;
  }
  .cover__title span { display: block; }
  .cover__blurb {
    position: absolute;
    left: 0; right: 0; top: 383px;
    font-family: "EB Garamond", Georgia, serif;
    font-size: 12.5px;
    line-height: 17px;
    color: var(--blurb);
  }
</style>
</head>
<body>
<main class="board">
  <article class="cover cover--white-orange">
    <p class="cover__author">Marcus Tindall</p>
    <div class="cover__rule cover__rule--top"></div>
    <h1 class="cover__title"><span>The</span><span>Lantern</span><span>Pact</span></h1>
    <div class="cover__rule cover__rule--bottom"></div>
    <p class="cover__blurb">Get clarity, focus, and a new zest for life<br>by following the lantern pact for just 21 days</p>
  </article>

  <article class="cover cover--white-green">
    <p class="cover__author">Marcus Tindall</p>
    <div class="cover__rule cover__rule--top"></div>
    <h1 class="cover__title"><span>The</span><span>Lantern</span><span>Pact</span></h1>
    <div class="cover__rule cover__rule--bottom"></div>
    <p class="cover__blurb">Get clarity, focus, and a new zest for life<br>by following the lantern pact for just 21 days</p>
  </article>

  <article class="cover cover--green">
    <p class="cover__author">Marcus Tindall</p>
    <div class="cover__rule cover__rule--top"></div>
    <h1 class="cover__title"><span>The</span><span>Lantern</span><span>Pact</span></h1>
    <div class="cover__rule cover__rule--bottom"></div>
    <p class="cover__blurb">Get clarity, focus, and a new zest for life<br>by following the lantern pact for just 21 days</p>
  </article>

  <article class="cover cover--red">
    <p class="cover__author">Marcus Tindall</p>
    <div class="cover__rule cover__rule--top"></div>
    <h1 class="cover__title"><span>The</span><span>Lantern</span><span>Pact</span></h1>
    <div class="cover__rule cover__rule--bottom"></div>
    <p class="cover__blurb">Get clarity, focus, and a new zest for life<br>by following the lantern pact for just 21 days</p>
  </article>
</main>
</body>
</html>
```